Stationary for Beauty and Spa School

Create a business card, letterhead and envelopes (primarily #10 envelope with and without window and catalog envelope) for a beauty and wellness school in Miami, Fl. We offer 8 different programs of study and need an eye catching look. Looking for a combination of modern yet sophisticated. Nothing corporate or business looking. Would like to have a look and feel that is similar (or incorporates aspects) of a new website we will be launching in the next 30 days (screen shot attached.)

The final design should communicate style and elegance in a down to earth and friendly way. We strive to provide our students with quality education, friendly and amicable staff and experienced instructors.
Updates

Hello. FYI, in order to print an aesthetically appealing business card, we would like to print them (the business cards) using silk printing method, with spot UV coating (on some elements, maybe the logo, or depending on the design) and die cuts. Please think of this when preparing your design.

Only 1 day left, please submit your designs for selection. Thanks

Target Market(s)

Adults 18-49 years who are mostly interested in beauty and fashion. Need a youthful & modern look, yet sophisticated and elegant.

Industry/Entity Type

School

Colors
e34197
6b449b
add136
f79021

Requirements
Must have
• Similar look and feel as website (see attached screen shot)
Same look and feel of website (see attached screenshot)
Logo
Address: 5126 NW 14th Avenue. Miami, Fl 33157
Telephone: 305-914-3062
Fax: 786-552-4190
website/url: www.lumaroveacademy.edu
incorporate Photo of blonde model (attached)
Nice to have
• Tag line: "Beautify your future." Also, maybe two-sided business card. Would be nice if we could mention our programs (maybe in the back of the card). Below are the program offerings (names cannot be changed but order is irrelevant)... Cosmetology, Barber, Spa Therapy, Massage Therapy, Makeup Artistry, Skin Care, Manicure, Pedicure & Nail Extensions, Full Specialist.

A design with text plus a beautiful photo of a model is appealing. Attached to the files is a sample of a cover for a student handbook we have created. You should use the photo of the blonde model (attached) in your design. The original (quality) version of this stock photograph has been uploaded.

Also would be nice to request clients to follow us on facebook and instagram by including the icons.
Should not have
• A corporate or business look. We are a vocational school teaching beauty and spa programs and we like our advertising to have a look that resembles the industry. We do not want a very serious look or snobby feel.

```html
<!DOCTYPE html>
<html lang="en">
<head>
<meta charset="utf-8">
<title>Lumarove Academy – Business Card</title>
<link rel="stylesheet" href="https://fonts.googleapis.com/css2?family=Open+Sans:wght@300;400;600&display=swap">
<style>
  :root {
    --bg: #e8eff1;
    --paper: #ffffff;
    --ink: #111111;
    --pink: #e84593;
    --purple: #6d4096;
    --orange: #f58b2e;
    --green: #9ccb3b;
    --on-color: #ffffff;
  }
  * { margin: 0; padding: 0; box-sizing: border-box; }
  html, body {
    width: 1200px; height: 1000px; overflow: hidden;
    background: var(--bg);
    font-family: "Open Sans", Arial, sans-serif;
  }
  .canvas { position: relative; width: 1200px; height: 1000px; }

  .card { position: absolute; top: 20px; height: 542px; }

  /* Front */
  .card-front { left: 263px; width: 307px; background: var(--paper); }
  .card-front .brand {
    position: absolute; right: 61px; top: 86px;
    white-space: nowrap; text-align: right;
    font-weight: 600; font-size: 23px; color: var(--ink);
  }
  .card-front .person {
    position: absolute; right: 61px; top: 267px; text-align: right; color: var(--ink);
  }
  .person .name { font-size: 22.5px; font-weight: 600; line-height: 28px; }
  .person .role { font-size: 18.5px; font-weight: 300; line-height: 22px; }
  .card-front .tagline {
    position: absolute; right: 61px; top: 489px;
    font-size: 18.5px; font-weight: 300; color: var(--ink);
  }
  .stripe { position: absolute; right: 0; top: 0; width: 43px; height: 100%; display: flex; flex-direction: column; }
  .stripe span { flex: 1 1 0; }

  /* Back */
  .card-back { left: 631px; width: 307px; display: flex; flex-direction: column; color: var(--on-color); font-weight: 300; }
  .back-band {
    flex: none; height: 25%; overflow: hidden;
    padding-left: 30px; font-size: 18.5px; line-height: 25px;
  }
  .pink { background: var(--pink); }
  .purple { background: var(--purple); }
  .orange { background: var(--orange); }
  .green { background: var(--green); }
  .programs { list-style: none; }
  .programs li { position: relative; padding-left: 15px; }
  .programs li::before { content: "•"; position: absolute; left: 0; font-size: 13px; }
  .band-pink { padding-top: 33px; }
  .band-purple { padding-top: 3px; }
  .contact { padding-top: 24px; line-height: 22.7px; }
  .web { display: flex; align-items: center; font-size: 20px; padding-bottom: 6px; white-space: nowrap; }
</style>
</head>
<body>
<main class="canvas">
  <section class="card card-front">
    <div class="brand">Lumarove Academy</div>
    <div class="person">
      <div class="name">Name Surname</div>
      <div class="role">position</div>
    </div>
    <div class="tagline">Beautify your future</div>
    <div class="stripe">
      <span class="pink"></span><span class="purple"></span><span class="orange"></span><span class="green"></span>
    </div>
  </section>

  <section class="card card-back">
    <div class="back-band band-pink pink">
      <ul class="programs">
        <li>Cosmetology</li><li>Barber</li><li>Spa Therapy</li><li>Skin Care</li>
      </ul>
    </div>
    <div class="back-band band-purple purple">
      <ul class="programs">
        <li>Manicure</li><li>Massage Therapy</li><li>Makeup Artistry</li><li>Pedicure &amp; Nail Extensions</li><li>Full Specialist</li>
      </ul>
    </div>
    <div class="back-band contact orange">
      5126 NW 14th Avenue.<br>
      Miami, Fl 33157<br>
      Telephone: 305-914-3062<br>
      Fax: 786-552-4190
    </div>
    <div class="back-band web green">www.lumaroveacademy.edu</div>
  </section>
</main>
</body>
</html>
```